Hispanic Financial Counseling and Advocate Firm seeks business card design

Looking for a clean, professional business card design. This is a firm that specializes in providing financial education, coaching, and planning to the Hispanic community. The name of the company is Valemar, which means to prosper. We need a design that is clean, professional, and invokes trust, professionalism, but also welcoming. Our logo is a plant growing from a hand to give the messaging of of being in control of growing your financial future and security. Its part of a larger organization names Celesta Financial Group, who's logo is a tree with multi colored branches. We have the back of the card designed so we just need the front designed. the back is blue, so front needs to be a different background color, not blue.

Target Market(s)

Hispanic Community looking to better their future

Industry/Entity Type

financial services

Contact Information for Business Card

contact info: Anselmo Ibarra Jr, 951-555-0147, info@celestafinancialgroup.example. Celestafinancialgroup.example. tag line: Para un futuro mas seguro!

Requirements
Must have
• basics: logo, contact info.
Nice to have
• possibly incorporate the tree logo provided somehow
Should not have
• should not look like the back, needs to be different from the back provided.

```html
<!DOCTYPE html>
<html lang="es">
<head>
<meta charset="utf-8">
<title>Valemar – Tarjeta de presentación</title>
<link href="https://fonts.googleapis.com/css2?family=Montserrat:wght@400;500;700&display=swap" rel="stylesheet">
<style>
  :root{
    --stage:#1d1e20;
    --navy:#032b40;
    --slate:#4a5775;
    --white:#ffffff;
    --green:#6ab23e;
    --leaf-green:#8cc63f;
    --leaf-blue:#29a8e0;
    --leaf-purple:#9b7cc2;
    --leaf-red:#e8433e;
    --leaf-yellow:#f6c21c;
  }
  *{box-sizing:border-box;margin:0;padding:0}
  html,body{width:1200px;height:852px;overflow:hidden;background:var(--stage)}
  body{position:relative;font-family:"Montserrat",Arial,sans-serif;color:var(--white)}

  .card{position:absolute;width:560px;height:320px;box-shadow:0 18px 40px rgba(0,0,0,.45)}

  /* Back of card */
  .card--back{left:80px;top:80px;background:var(--navy)}
  .brand{position:absolute;left:70px;top:70px;display:flex;align-items:center;gap:22px}
  .brand__dot{width:74px;height:74px;border-radius:50%;background:var(--white)}
  .brand__divider{width:1.5px;height:96px;background:var(--white)}
  .brand__name{font-weight:500;font-size:34px;line-height:1.1;letter-spacing:.2px}
  .brand__name span{display:block;font-size:19px}
  .services{position:absolute;left:70px;top:208px;font-size:15px;line-height:1.5;font-weight:400}
  .services li{list-style:none;display:inline-flex;align-items:center;margin-right:10px}
  .services .row{display:block}
  .bullet{width:8px;height:8px;border-radius:50% 0 50% 50%;margin-right:6px;transform:rotate(-45deg)}
  .bullet--green{background:var(--leaf-green)}
  .bullet--blue{background:var(--leaf-blue)}
  .bullet--red{background:var(--leaf-red)}
  .bullet--purple{background:var(--leaf-purple)}
  .bullet--yellow{background:var(--leaf-yellow)}

  /* Front of card */
  .card--front{left:560px;top:452px;background:var(--slate)}
  .tagline{position:absolute;left:40px;top:40px;font-weight:700;font-size:21px;letter-spacing:1.5px}
  .person{position:absolute;left:40px;top:150px}
  .person__name{font-weight:700;font-size:22px;letter-spacing:1.5px;color:var(--green)}
  .person__role{font-size:15px;margin-top:2px}
  .contact{position:absolute;left:40px;top:222px;display:flex;gap:12px}
  .contact__icons{display:flex;flex-direction:column;gap:8px;padding-top:3px}
  .contact__icons svg{width:14px;height:14px;display:block}
  .contact__rule{width:1px;background:var(--green)}
  .contact__lines{font-size:15px;line-height:22px}
  .sub-brand{position:absolute;right:40px;top:150px;display:flex;align-items:center;gap:10px}
  .sub-brand__dot{width:22px;height:22px;border-radius:50%;background:var(--green)}
  .sub-brand__name{font-weight:500;font-size:30px;color:var(--green)}
</style>
</head>
<body>

<section class="card card--back" aria-label="Reverso de la tarjeta">
  <div class="brand">
    <div class="brand__dot"></div>
    <div class="brand__divider"></div>
    <div class="brand__name">Celesta<span>Financial Group Inc</span></div>
  </div>
  <ul class="services">
    <span class="row">
      <li><i class="bullet bullet--green"></i>Inmigración</li>
      <li><i class="bullet bullet--blue"></i>Planificacion Financiera</li>
    </span>
    <span class="row">
      <li><i class="bullet bullet--red"></i>Seguros</li>
      <li><i class="bullet bullet--purple"></i>Impuestos</li>
      <li><i class="bullet bullet--red"></i>Y mas</li>
    </span>
    <span class="row">
      <li><i class="bullet bullet--yellow"></i>Preparación de documentos</li>
    </span>
  </ul>
</section>

<section class="card card--front" aria-label="Frente de la tarjeta">
  <p class="tagline">PARA UN FUTURO MAS SEGURO</p>
  <div class="person">
    <p class="person__name">ANSELMO IBARRA JR.</p>
    <p class="person__role">Managing Director</p>
  </div>
  <div class="contact">
    <div class="contact__icons">
      <svg viewBox="0 0 16 16" aria-hidden="true"><path fill="#6ab23e" d="M3 1l3 3-1.5 2a9 9 0 0 0 5.5 5.5L12 10l3 3-2 2C7 15 1 9 1 3z"/></svg>
      <svg viewBox="0 0 16 16" aria-hidden="true"><rect x="1.5" y="3.5" width="13" height="9" fill="none" stroke="#6ab23e" stroke-width="1.5"/><path d="M1.5 3.5L8 9l6.5-5.5" fill="none" stroke="#6ab23e" stroke-width="1.5"/></svg>
      <svg viewBox="0 0 16 16" aria-hidden="true"><circle cx="8" cy="8" r="6.5" fill="none" stroke="#6ab23e" stroke-width="1.5"/><path d="M1.5 8h13M8 1.5c-3 3.5-3 9.5 0 13M8 1.5c3 3.5 3 9.5 0 13" fill="none" stroke="#6ab23e" stroke-width="1.2"/></svg>
    </div>
    <div class="contact__rule"></div>
    <div class="contact__lines">
      <p>951-555-0147</p>
      <p>info@celestafinancialgroup.example</p>
      <p>www.celestafinancialgroup.example</p>
    </div>
  </div>
  <div class="sub-brand">
    <div class="sub-brand__dot"></div>
    <span class="sub-brand__name">Valemar</span>
  </div>
</section>

</body>
</html>
```